Personal Development Book for Millennials Needs a Cover Design

Book Title: Salt Horizon: A Dreamer's Map to Being, 15 "No Escape" Queries on Joy, Routines and Grit for Muddled Millennials
Author's Name: Marcus T. Oldenfrey
Salt Horizon: A Dreamer's Map to Being is a collection of raw, unfiltered and personal essays on happiness, habits and hustle. It is a compilation of 15 provocative, yet fundamental questions that every mixed-up millennial or twenty-something should answer in order to live a life full of energy and excitement rather than monotony and mediocrity.
It is a personal development book written by a regular, twenty-something dude who got tired of doing boring things. He then quit his job, fell off a motorcycle somewhere near the equator, and came back to the States and immediately started writing.
"Pura vida," the law of the land in Costa Rica, translates to "pure life." "Pura vida" is more than just a greeting; it is an embodiment of the Costa Rican people, who find immense happiness in life's little pleasures, preferring to lay low, live slow and live purposefully. "Pura vida" is another way of saying "relax and take it easy."
The goal of the book is to stand out on the Zelvora platform as a small thumbnail. The imagery should make the viewer feel that the book (and the author) is an authority on the topic of self-discovery, self-awareness, and purposeful, intentional living.
The reader should feel that they MUST read this book if they are the least bit confused, anxious, mixed-up or desperately trying to figure out how to take back control of their own life and start doing the things that excite them. It's more important that the book "pops off the shelf" or stands out and catches the eye quickly.
The most important part of the design is that it is clean, uncluttered and simple. It should embody the "pura vida" lifestyle. I am open to any image or illustration you choose.
I like a bold color palette, and I'd like to see green be the primary color used in the design. Lush, greenery is everywhere in Costa Rica. Green also represents life, very appropriate for this book. I like bold titles that are easy to recognize and comprehend. Please use no more than 2-3 colors.
Zelvora eBook covers I particularly like:
Print Liftoff by Wesley Harrow
A Man Near The Pier by Neil Dorsey
Inner Steel — 48 Tested Paths to Build Inner Steel, Lift Your Morale and Quiet Inner Worry by Rory M.T. Pask
Hour Mastery: Peak Output by Owen Farrukh
Target Market(s)
Millennials
Requirements
Must have
- This book is intended to encourage millennials to do some soul-searching, think and WRITE down their own answers to the questions in this book. It is a book that should be read with a notebook and a pen close by.
- I'd like to see covers that subtly hint at this fact. Please reference the example covers listed in the project description to best match the style of cover I am looking for. If it is clear that you have NOT referenced the example covers, your design will be eliminated.
Nice to have
- If possible, would like to see designs that include the following three components WITHOUT making the cover feel too busy or cluttered:
- 1) Pen
- 2) Paper
- 3) Beach
Should not have
- Cover should NOT look or feel as if this is a book about environmentalism. Trees, plants, greenery, etc. should NOT be the primary focal point of the cover design. If included, these elements should be additive.

```html
<!DOCTYPE html>
<html lang="en">
<head>
<meta charset="utf-8">
<title>Salt Horizon: A Dreamer's Map to Being</title>
<link rel="stylesheet" href="https://fonts.googleapis.com/css2?family=Lobster+Two:ital,wght@1,700&family=Oswald:wght@500;700&display=swap">
<style>
  :root {
    --lime-light: #e9f06c;
    --lime: #b9d83c;
    --leaf: #5f9a2a;
    --forest: #2d5e1d;
    --forest-deep: #1f4414;
    --sky-blue: #2b9fdb;
    --hammock-blue: #3f8fd0;
    --hammock-deep: #1d5f9e;
    --navy: #16324a;
    --white: #ffffff;
  }
  * { margin: 0; padding: 0; box-sizing: border-box; }
  html, body { width: 800px; height: 1200px; overflow: hidden; }
  body { background: var(--forest-deep); }
  .cover {
    position: relative;
    width: 800px;
    height: 1200px;
    overflow: hidden;
    background: radial-gradient(ellipse 75% 60% at 50% 45%, var(--lime-light) 0%, var(--lime) 45%, var(--leaf) 82%, var(--forest) 100%);
    text-align: center;
  }
  .title {
    position: absolute;
    top: 40px;
    left: 0;
    width: 100%;
    font-family: "Lobster Two", cursive;
    font-style: italic;
    font-weight: 700;
    color: var(--sky-blue);
    line-height: 0.9;
    -webkit-text-stroke: 3px var(--white);
    paint-order: stroke fill;
    text-shadow: 0 6px 10px rgba(20, 60, 20, 0.3);
  }
  .title-line { display: block; }
  .title-line--first { font-size: 270px; }
  .title-line--second { font-size: 225px; }
  .tagline {
    position: absolute;
    top: 585px;
    left: 30px;
    right: 30px;
    font-family: "Oswald", sans-serif;
    font-weight: 500;
    font-size: 54px;
    letter-spacing: 1px;
    color: var(--navy);
    text-transform: uppercase;
  }
  .subtitle {
    position: absolute;
    top: 680px;
    left: 60px;
    right: 60px;
    font-family: "Oswald", sans-serif;
    font-weight: 500;
    font-size: 27px;
    line-height: 1.3;
    color: var(--navy);
    text-transform: uppercase;
  }
  .scene-art {
    position: absolute;
    top: 770px;
    left: 0;
    width: 800px;
    height: 260px;
    background:
      radial-gradient(ellipse 30% 38% at 50% 60%, var(--hammock-blue) 0%, var(--hammock-deep) 60%, rgba(29, 95, 158, 0) 100%),
      radial-gradient(ellipse 60% 50% at 50% 55%, rgba(233, 240, 108, 0.5), rgba(95, 154, 42, 0) 100%);
  }
  .ground {
    position: absolute;
    left: 0;
    bottom: 0;
    width: 800px;
    height: 200px;
  }
  .author {
    position: absolute;
    bottom: 68px;
    left: 0;
    width: 100%;
    font-family: "Oswald", sans-serif;
    font-weight: 500;
    font-size: 44px;
    letter-spacing: 2px;
    color: var(--white);
    text-transform: uppercase;
  }
</style>
</head>
<body>
  <main class="cover">
    <h1 class="title">
      <span class="title-line title-line--first">Salt</span>
      <span class="title-line title-line--second">Horizon</span>
    </h1>
    <p class="tagline">A Dreamer's Map to Being</p>
    <p class="subtitle">15 "No Escape" Queries on Joy, Routines and Grit<br>for Muddled Millennials</p>
    <div class="scene-art" role="img" aria-label="Illustration of a relaxed man in a shirt and tie lying in a blue hammock strung between palm trees on a beach"></div>
    <svg class="ground" viewBox="0 0 800 200" aria-hidden="true">
      <path d="M0 50 Q400 -10 800 50 L800 200 L0 200 Z" fill="var(--leaf)" opacity="0.7"/>
      <path d="M0 80 Q400 20 800 80 L800 200 L0 200 Z" fill="var(--forest)" opacity="0.85"/>
    </svg>
    <p class="author">Marcus T. Oldenfrey</p>
  </main>
</body>
</html>
```